Unique & Creative Business Card for Lumavessence

Would you please create a unique design that is soft and appealing to people who seek to raise vibrational energy for themselves, for animals (domestic or wild), or for the environment.

Optional: Elements could include, landscapes, wild animals, feathers, vibrational patterns, the elements (Earth, water, fire, air and space). Images that are calming.

With Thanks!

Target Market(s)

People and businesses who are into the environment, animal welfare, alternative health.

Contact Information for Business Card

Moira Bell
Energist
mb@lumavessence.example
lumavessence.example

Requirements
Must have
• Lumavessence logo (attached)
Symbols that represent our main services: Natural environment, animal, human and energy.
Our strapline ‘Finding Your Resonant Balance’
Nice to have
• Clear and easy to read
Colours based on nature/soft colours

```html
<!DOCTYPE html>
<html lang="en">
<head>
<meta charset="utf-8">
<title>Lumavessence Business Card</title>
<link rel="stylesheet" href="https://fonts.googleapis.com/css2?family=Archivo+Black&family=Montserrat:wght@400;500;800&display=swap">
<style>
  :root {
    --bg: #ecebef;
    --card: #ffffff;
    --navy: #2a4a8e;
    --ring: #4f79b8;
    --lilac: #e4dbea;
    --teal: #2fb7a0;
    --teal-deep: #1d6b5b;
    --forest-a: #a9c9bd;
    --forest-b: #9f9aab;
    --ink: #2b2b33;
    --white: #ffffff;
  }
  * { box-sizing: border-box; margin: 0; padding: 0; }
  html, body { width: 1200px; height: 900px; overflow: hidden; }
  body {
    background: var(--bg);
    display: flex;
    flex-direction: column;
    align-items: center;
    justify-content: center;
    gap: 44px;
    font-family: "Montserrat", sans-serif;
  }
  .card {
    position: relative;
    width: 640px;
    height: 366px;
    background: var(--card);
    overflow: hidden;
    box-shadow: 0 6px 22px rgba(40, 40, 70, 0.18);
  }

  /* Back: services */
  .services {
    position: absolute;
    top: 46px;
    left: 0;
    right: 0;
    display: flex;
    justify-content: center;
    align-items: flex-start;
    gap: 40px;
  }
  .service { display: flex; flex-direction: column; align-items: center; width: 156px; }
  .service-badge {
    width: 110px;
    height: 110px;
    border-radius: 50%;
    border: 3px solid var(--ring);
    display: flex;
    align-items: center;
    justify-content: center;
    background: var(--card);
  }
  .service-icon {
    width: 90px;
    height: 90px;
    border-radius: 50%;
    background: radial-gradient(circle, var(--teal) 0 30%, var(--teal-deep) 31% 40%, var(--lilac) 41%);
  }
  .service-label {
    margin-top: 14px;
    font-weight: 800;
    font-size: 15px;
    letter-spacing: 0.06em;
    line-height: 1.15;
    color: var(--navy);
    text-align: center;
    text-transform: uppercase;
  }
  .forest {
    position: absolute;
    left: 0;
    right: 0;
    bottom: 0;
    height: 120px;
    background: linear-gradient(180deg, rgba(255,255,255,0) 0%, var(--forest-a) 55%, var(--forest-b) 100%);
    opacity: 0.75;
  }

  /* Front: contact */
  .identity { position: absolute; top: 46px; left: 44px; }
  .person-name {
    font-family: "Archivo Black", sans-serif;
    font-size: 28px;
    line-height: 1.1;
    letter-spacing: 0.02em;
    color: var(--navy);
    text-transform: uppercase;
  }
  .person-role { font-size: 18px; color: var(--ink); margin-top: 2px; }

  .brand {
    position: absolute;
    top: 44px;
    right: 30px;
    display: flex;
    align-items: center;
    gap: 10px;
  }
  .brand-mark {
    width: 48px;
    height: 48px;
    border-radius: 50%;
    background: var(--lilac);
    border: 3px solid var(--ring);
  }
  .brand-name {
    font-size: 21px;
    font-weight: 500;
    color: var(--navy);
    text-transform: uppercase;
    letter-spacing: 0.03em;
  }

  .contact {
    position: absolute;
    top: 156px;
    left: 44px;
    list-style: none;
    display: flex;
    flex-direction: column;
    gap: 6px;
  }
  .contact-item {
    display: flex;
    align-items: center;
    gap: 10px;
    font-size: 17px;
    line-height: 1.2;
    color: var(--ink);
  }
  .contact-item svg { width: 18px; height: 18px; flex: none; }

  .wave { position: absolute; left: 0; top: 0; width: 640px; height: 366px; }
  .strapline {
    position: absolute;
    right: 30px;
    bottom: 24px;
    font-size: 18px;
    font-weight: 500;
    color: var(--white);
    letter-spacing: 0.03em;
    text-transform: uppercase;
  }
</style>
</head>
<body>

  <section class="card card-back">
    <div class="services">
      <div class="service">
        <div class="service-badge"><div class="service-icon" role="img" aria-label="Leaf and globe icon for natural environment"></div></div>
        <p class="service-label">Natural<br>Environment</p>
      </div>
      <div class="service">
        <div class="service-badge"><div class="service-icon" role="img" aria-label="Bear icon for animal"></div></div>
        <p class="service-label">Animal</p>
      </div>
      <div class="service">
        <div class="service-badge"><div class="service-icon" role="img" aria-label="Radiant sun icon for human and energy"></div></div>
        <p class="service-label">Human and<br>Energy</p>
      </div>
    </div>
    <div class="forest" role="img" aria-label="Soft watercolour forest treeline"></div>
  </section>

  <section class="card card-front">
    <svg class="wave" viewBox="0 0 640 366" aria-hidden="true">
      <path d="M0 264 C210 300 430 232 640 130" fill="none" stroke="#e4dbea" stroke-width="12"/>
      <path d="M0 280 C220 312 440 242 640 150 L640 366 L0 366 Z" fill="#2a4a8e"/>
    </svg>

    <div class="identity">
      <h1 class="person-name">Moira Bell</h1>
      <p class="person-role">Energist</p>
    </div>

    <div class="brand">
      <span class="brand-mark"></span>
      <span class="brand-name">Lumavessence</span>
    </div>

    <ul class="contact">
      <li class="contact-item">
        <svg viewBox="0 0 24 24"><path d="M6.6 10.8a15 15 0 0 0 6.6 6.6l2.2-2.2a1 1 0 0 1 1-.25 11.4 11.4 0 0 0 3.6.57 1 1 0 0 1 1 1V20a1 1 0 0 1-1 1A17 17 0 0 1 3 4a1 1 0 0 1 1-1h3.5a1 1 0 0 1 1 1c0 1.25.2 2.45.57 3.6a1 1 0 0 1-.25 1z" fill="#2a4a8e"/></svg>
        5550104821
      </li>
      <li class="contact-item">
        <svg viewBox="0 0 24 24"><rect x="2" y="5" width="20" height="14" fill="#2a4a8e"/><path d="M2 5l10 8 10-8" fill="none" stroke="#fff" stroke-width="1.6"/></svg>
        mb@lumavessence.example
      </li>
      <li class="contact-item">
        <svg viewBox="0 0 24 24" fill="none" stroke="#2a4a8e" stroke-width="1.8"><circle cx="12" cy="12" r="9"/><path d="M3 12h18M12 3c3 3 3 15 0 18M12 3c-3 3-3 15 0 18"/></svg>
        www.lumavessence.example
      </li>
    </ul>

    <p class="strapline">Finding Your Resonant Balance</p>
  </section>

</body>
</html>
```